Flyer Fewo Dorn
Trotz etlicher Änderungen immer Hilfsbereit und alle Wünsche wurden von Jonas 1A umgesetzt.
Sehr geehrte Damen und Herren, 01.12.25
wir werden jetzt gleich die Entscheidung treffen. Daher möchten wir uns bei Ihnen allen für die Entwürfe und gute Zusammenarbeit bedanken. Es war für uns recht schwierig den Gewinner festzulegen.
Mit freundlichen Grüßen
Familie Dorn
Sehr geehrte Damen und Herren,
Nachtrag. Bitte weisen Sie auf das:
1. Hügeltaler Kirschenfest vom 21.02.26 - 06.04.26
2. Oldimerveranstaltungen
3. Ausschrank Federweiser / neuer Wein ab September 2026
4. viele regionale Weinfeste
hin.
zunächst möchten wir uns bei Ihnen für die bisherigen Entwürfe bedanken. Wir haben eben die Textdatei überarbeitet und neu abgespeichert. Bitte überarbeiten Sie Ihre Texte in den Entwürfen. Sie können auch gerne textliche Passagen kürzer fassen.
Wir bitten Sie, die Weinregion südliche Weinstrasse etwas mehr im Hintergrund hervorzuheben.
Wir melden uns wenn dann nach der Überarbeitung der Texte.
Mit freundlichem Gruß
Aufgabenstellung
Warmes Design, bezogen auf die Weinregion, hoher Freizeitwert, zentral gelegen. Bodenständig, da die Wohnung in einem Haus ausgebaut ist was keinerlei Grautöne hat. Das 2 Familienhaus ist im italienischen Stil gebaut

```html
<!DOCTYPE html>
<html lang="de">
<head>
<meta charset="utf-8">
<title>Ferienwohnung Dorn – Flyer</title>
<link href="https://fonts.googleapis.com/css2?family=Playfair+Display:ital,wght@0,700;1,400;1,700&display=swap" rel="stylesheet">
<style>
  :root{
    --terracotta:#c07563;
    --text:#5a5a5a;
    --text-strong:#3f3f3f;
    --paper:#ffffff;
  }
  *{margin:0;padding:0;box-sizing:border-box}
  html,body{width:1200px;height:848px;overflow:hidden;background:var(--paper)}
  .flyer{position:relative;width:1200px;height:848px;background:var(--paper);
    font-family:"Playfair Display",Georgia,serif;color:var(--text)}
  .band{position:absolute;left:0;width:1200px;background:var(--terracotta)}
  .band--top{top:0;height:12px}
  .band--bottom{bottom:0;height:21px}
  .heading{position:absolute;font-weight:700;color:var(--terracotta);text-transform:uppercase;
    font-size:19px;line-height:26px;letter-spacing:0.1px}
  .photo{position:absolute;border-radius:4px}
  .photo--living{left:44px;top:72px;width:261px;height:183px;
    background:linear-gradient(160deg,#f3efe9 0%,#e6ddd2 55%,#b98d66 100%)}
  .photo--house{left:311px;top:72px;width:248px;height:183px;
    background:linear-gradient(180deg,#5d9be0 0%,#f1ede4 40%,#d8c7b1 75%,#b78f7c 100%)}
  .photo--bedroom{left:44px;top:262px;width:232px;height:213px;
    background:linear-gradient(135deg,#f3ece3 0%,#e9e4de 50%,#b58456 100%)}
  .photo--bath{left:285px;top:262px;width:274px;height:211px;
    background:linear-gradient(160deg,#efe2cf 0%,#e7d5bf 60%,#c09066 100%)}
  .prose{position:absolute;font-style:italic;font-size:16.4px;line-height:23.6px}
  .prose b{font-weight:700;color:var(--text-strong)}
  .prose p + p{margin-top:23.6px}
  .features{list-style:none}
  .features li::before{content:"\2713\00a0";font-style:normal}
</style>
</head>
<body>
<div class="flyer">
  <div class="band band--top"></div>

  <h1 class="heading" style="left:44px;top:38px">Willkommen in der Ferienwohnung Dorn!</h1>

  <div class="photo photo--living" role="img" aria-label="Foto: Wohn- und Essbereich mit Sofa, Fernseher und gedecktem Esstisch"></div>
  <div class="photo photo--house" role="img" aria-label="Foto: Mediterranes Zweifamilienhaus mit Holztür und Vorgarten"></div>
  <div class="photo photo--bedroom" role="img" aria-label="Foto: Schlafzimmer mit Bett und großem Kleiderschrank mit TV"></div>
  <div class="photo photo--bath" role="img" aria-label="Foto: Helles Bad mit Eckwanne, Waschtisch und Handtuchheizkörper"></div>

  <h2 class="heading" style="left:43px;top:486px;line-height:28px">Genießen Sie die Toskana der Pfalz –<br>stilvoll, modern &amp; mitten in den Weinbergen</h2>

  <div class="prose" style="left:44px;top:545px;width:520px">
    <p>In einem <b>mediterranen 2-Familienhaus</b>, umgeben von <b>Weinreben</b>, erwartet Sie unsere moderne, gemütlich eingerichtete Ferienwohnung im Obergeschoss. Von hier aus starten Sie zu <b>Spaziergängen und Radtouren</b>, genießen <b>prämierte Weingüter</b> und Restaurants mit gemütlichen Freisitzen und das milde Klima der <b>„Toskana der Pfalz“</b>.</p>
    <p>Edesheim und Edenkoben bieten alle <b>Einkaufsmöglichkeiten</b> des täglichen Bedarfs, der <b>Pfälzerwald</b> ist nach ca. 10 km erreichbar. Auch Ausflüge nach <b>Speyer</b>, ins <b>Elsass</b> oder zum <b>Deutschen Weintor</b> lassen sich von hier wunderbar planen.</p>
  </div>

  <h2 class="heading" style="left:647px;top:38px">Ihre Ausstattung im Überblick</h2>

  <ul class="prose features" style="left:644px;top:78px;width:500px">
    <li>Privater <b>Haus- &amp; Wohnungseingang</b></li>
    <li><b>76 m² lichtdurchflutete</b> Wohnung</li>
    <li>Großzügiges <b>Wohn-/Esszimmer</b> mit Schlafcouch</li>
    <li>Moderne <b>Lindgart-Einbauküche</b> mit Insel &amp; Kaffeevollautomat</li>
    <li>Schlafzimmer mit <b>Boxspringbett</b> und 3-m-Kleiderschrank inkl. TV</li>
    <li>Großes Bad mit <b>Wanne &amp; Dusche</b> mit Sitzbank</li>
    <li>Zwei <b>überdachte Balkone</b> – Sonne &amp; Sonnenuntergänge genießen</li>
    <li>Waschmaschine, Abstellraum, <b>kostenloses WLAN</b></li>
    <li><b>PKW-Stellplatz</b> am Haus, <b>E-Bike-Abstellplatz</b> in der Garage</li>
    <li><b>Fußbodenheizung</b> &amp; LED-Beleuchtung</li>
    <li>Nichtraucher – Rauchen auf dem Balkon erlaubt</li>
    <li>Hunde nach Absprache erlaubt (max. 1)</li>
  </ul>

  <h2 class="heading" style="left:644px;top:422px">Erleben Sie die Weinregion Südliche<br>Weinstrasse</h2>

  <div class="prose" style="left:644px;top:484px;width:505px">
    <p><b>Hügeltaler Kirschenfest vom 21.02.–06.04.2026 –</b> zartrosa Blüten, geöffnete Winzerhöfe und erste Frühlingssonne entlang der Südlichen Weinstraße.</p>
    <p><b>Stimmungsvolle Oldtimer-Veranstaltungen in der Region</b> – liebevoll restaurierte Fahrzeuge vor Weinbergen und historischen Ortsbildern.</p>
    <p><b>Ausschank von Federweißer und neuem Wein ab September</b> – herbstliche Genusszeit in gemütlichen Weingütern der Umgebung.</p>
    <p style="margin-top:23px"><b>Zahlreiche regionale Weinfeste</b> – gesellige Abende mit gutem Wein, Musik und Pfälzer Spezialitäten in den umliegenden Orten.</p>
  </div>

  <div class="band band--bottom"></div>
</div>
</body>
</html>
```